Präsentationsvorlagen / Powerpoint Master for my company
Zielgruppe
Offline hardware device to manage and save passwords safely.
Aufgabenstellung
DIN A4 quer

```html
<!DOCTYPE html>
<html lang="en">
<head>
<meta charset="utf-8">
<title>KeyHaven – Presentation Master</title>
<link href="https://fonts.googleapis.com/css2?family=Montserrat:wght@400;500;700&family=Source+Sans+3:wght@400;600&display=swap" rel="stylesheet">
<style>
  :root{
    --green:#2f6f3a;
    --green-deep:#2b6a36;
    --ink:#1e1e1e;
    --paper:#ffffff;
    --stage:#f2f2f2;
    --text:#222222;
    --photo-wood:#8a5a3a;
    --photo-office:#7f8a90;
  }
  *{box-sizing:border-box;margin:0;padding:0}
  html,body{width:882px;height:1200px;overflow:hidden;background:var(--stage)}
  body{position:relative;font-family:"Source Sans 3",sans-serif;color:var(--text)}

  .slide{position:absolute;background:var(--paper);overflow:hidden;box-shadow:0 3px 10px rgba(0,0,0,.18)}
  .slide--small{width:370px;height:262px}
  .slide--large{left:61px;top:620px;width:760px;height:537px}

  .heading{font-family:"Montserrat",sans-serif;font-weight:700;color:var(--green)}
  .brand{position:absolute;font-family:"Montserrat",sans-serif;font-weight:700;color:var(--ink);display:flex;align-items:center;gap:4px}
  .brand__dot{display:inline-block;background:var(--green)}
  .photo{position:absolute}
  .photo--wood{background:linear-gradient(135deg,#a06a43,var(--photo-wood) 55%,#5e3c26)}
  .photo--office{background:linear-gradient(135deg,#9aa6ad,var(--photo-office) 60%,#5d6a70)}
  .photo--desk{background:linear-gradient(135deg,#c9c2b8,#8d8f8f 60%,#5c5f60)}
  .photo--meeting{background:linear-gradient(135deg,#d9cfc4,#9c948a 60%,#5b6f5e)}

  .footer-title{position:absolute;font-family:"Montserrat",sans-serif;font-weight:700;color:var(--ink)}
  .footer-bar{position:absolute;left:0;right:0;bottom:0;display:flex}
  .footer-bar__green{background:var(--green)}
  .footer-bar__ink{flex:1;background:var(--ink)}
  .page-no{position:absolute;background:var(--ink);color:#fff;font-family:"Montserrat",sans-serif;font-weight:700;display:flex;align-items:center;justify-content:center}

  /* small slide shared sizes */
  .slide--small .page-title{position:absolute;left:26px;top:20px;font-size:15px}
  .slide--small .brand{right:20px;top:20px;font-size:13px}
  .slide--small .brand__dot{width:8px;height:8px}
  .slide--small .footer-title{left:26px;bottom:11px;font-size:6px}
  .slide--small .footer-bar{height:3px}
  .slide--small .footer-bar__green{width:115px}
  .slide--small .page-no{right:10px;bottom:4px;width:11px;height:14px;font-size:6px}
  .mini-head{font-family:"Montserrat",sans-serif;font-weight:700;color:var(--green);font-size:8px;margin-bottom:3px}
  .mini-text{font-size:5.5px;line-height:1.45;margin-bottom:6px}

  /* cover */
  .cover{left:56px;top:40px;background:var(--green)}
  .cover__photo{right:0;top:0;width:150px;height:190px;opacity:.85}
  .cover .brand{left:24px;top:82px;right:auto;color:#fff;font-size:17px}
  .cover .brand__dot{background:#fff;width:9px;height:9px}
  .cover__title{position:absolute;left:40px;top:116px;font-family:"Montserrat",sans-serif;color:#fff;font-size:15px;line-height:1.2}
  .cover__title strong{font-weight:700}
  .cover__rule{position:absolute;left:40px;top:160px;width:30px;height:1px;background:#fff}
  .cover__sub{position:absolute;left:40px;top:166px;font-family:"Montserrat",sans-serif;color:#fff;font-size:8px}
  .cover__body{position:absolute;left:40px;top:196px;width:210px;color:#fff;font-size:5.5px;line-height:1.45}

  /* slide 01 */
  .s01{left:456px;top:40px}
  .s01__img1{left:26px;top:58px;width:150px;height:72px}
  .s01__img2{left:26px;top:138px;width:150px;height:72px}
  .s01__col{position:absolute;left:196px;top:60px;width:150px}

  /* slide 02 */
  .s02{left:56px;top:320px}
  .s02__panel{position:absolute;left:0;top:0;bottom:0;width:170px;background:var(--green-deep);padding:22px 20px;color:#fff}
  .s02__panel .page-title{position:static;color:#fff;font-size:15px;margin-bottom:14px}
  .s02__panel .mini-head{color:#fff}
  .s02__panel .mini-text{color:#fff}
  .s02 .footer-title{color:#fff;z-index:1}
  .s02__img{left:190px;top:52px;width:158px;height:84px}
  .s02__col{position:absolute;left:190px;top:144px;width:158px}

  /* slide 03 small */
  .s03{left:456px;top:320px}
  .s03__img{left:0;top:48px;width:370px;height:118px}
  .s03__col{position:absolute;left:26px;top:176px;width:320px}

  /* large slide */
  .slide--large .page-title{position:absolute;left:72px;top:32px;font-size:31px}
  .slide--large .brand{right:34px;top:34px;font-size:28px}
  .slide--large .brand__dot{width:16px;height:16px}
  .large__photo{left:0;top:93px;width:760px;height:229px}
  .large__content{position:absolute;left:70px;top:345px;width:620px}
  .large__content .heading{font-size:20px;margin-bottom:10px}
  .large__content p{font-size:10.4px;line-height:1.48}
  .slide--large .footer-title{left:74px;bottom:17px;font-size:10.5px}
  .slide--large .footer-bar{height:7px}
  .slide--large .footer-bar__green{width:236px}
  .slide--large .page-no{right:37px;bottom:10px;width:21px;height:28px;font-size:11px}
</style>
</head>
<body>

<section class="slide slide--small cover">
  <div class="photo photo--meeting cover__photo" role="img" aria-label="Photo of a woman working at a laptop in an office"></div>
  <div class="brand"><span class="brand__dot"></span>KeyHaven</div>
  <h1 class="cover__title">Your Presentation<br><strong>Title Goes Here</strong></h1>
  <div class="cover__rule"></div>
  <p class="cover__sub">Your sub headline goes here</p>
  <p class="cover__body">Lorem ipsum dolor sit amet, consectetur adipiscing elit, sed do eiusmod tempor incididunt ut labore et dolore magna aliqua.</p>
</section>

<section class="slide slide--small s01">
  <h2 class="heading page-title">Page Title</h2>
  <div class="brand"><span class="brand__dot"></span>KeyHaven</div>
  <div class="photo photo--office s01__img1" role="img" aria-label="Photo of a team working in an open office"></div>
  <div class="photo photo--office s01__img2" role="img" aria-label="Photo of colleagues at a whiteboard"></div>
  <div class="s01__col">
    <h3 class="mini-head">Lorem ipsum</h3>
    <p class="mini-text">Lorem ipsum dolor sit amet, consectetur adipiscing elit, sed diam nonummy nibh euismod.</p>
    <h3 class="mini-head" style="margin-top:22px">Lorem ipsum</h3>
    <p class="mini-text">Lorem ipsum dolor sit amet, consectetur adipiscing elit, sed diam nonummy nibh euismod.</p>
  </div>
  <p class="footer-title">Presentation Title Goes Here</p>
  <div class="footer-bar"><span class="footer-bar__green"></span><span class="footer-bar__ink"></span></div>
  <div class="page-no">01</div>
</section>

<section class="slide slide--small s02">
  <div class="s02__panel">
    <h2 class="heading page-title">Page Title</h2>
    <h3 class="mini-head">Lorem ipsum</h3>
    <p class="mini-text">Lorem ipsum dolor sit amet, consectetur adipiscing elit, sed do eiusmod tempor incididunt ut labore et dolore magna aliqua.</p>
    <p class="mini-text">Lorem ipsum dolor sit amet, consectetur adipiscing elit, sed do eiusmod tempor incididunt ut labore et dolore magna aliqua.</p>
  </div>
  <div class="brand"><span class="brand__dot"></span>KeyHaven</div>
  <div class="photo photo--desk s02__img" role="img" aria-label="Photo of hands typing on a laptop"></div>
  <div class="s02__col">
    <p class="mini-text">Lorem ipsum dolor sit amet, consectetur adipiscing elit, sed do eiusmod tempor incididunt ut labore et dolore magna aliqua.</p>
    <p class="mini-text">Lorem ipsum dolor sit amet, consectetur adipiscing elit, sed diam nonummy nibh euismod.</p>
  </div>
  <p class="footer-title">Presentation Title Goes Here</p>
  <div class="footer-bar"><span class="footer-bar__green"></span><span class="footer-bar__ink"></span></div>
  <div class="page-no">02</div>
</section>

<section class="slide slide--small s03">
  <h2 class="heading page-title">Page Title</h2>
  <div class="brand"><span class="brand__dot"></span>KeyHaven</div>
  <div class="photo photo--wood s03__img" role="img" aria-label="Photo of a team stacking hands over a wooden desk"></div>
  <div class="s03__col">
    <h3 class="mini-head">Lorem ipsum</h3>
    <p class="mini-text">Lorem ipsum dolor sit amet, consectetur adipiscing elit, sed do eiusmod tempor incididunt ut labore et dolore magna aliqua.</p>
  </div>
  <p class="footer-title">Presentation Title Goes Here</p>
  <div class="footer-bar"><span class="footer-bar__green"></span><span class="footer-bar__ink"></span></div>
  <div class="page-no">03</div>
</section>

<section class="slide slide--large">
  <h2 class="heading page-title">Page Title</h2>
  <div class="brand"><span class="brand__dot"></span>KeyHaven</div>
  <div class="photo photo--wood large__photo" role="img" aria-label="Photo of a team stacking hands over a wooden desk with notebook, charts and laptop"></div>
  <div class="large__content">
    <h3 class="heading">Lorem ipsum</h3>
    <p>Lorem ipsum dolor sit amet, consectetur adipiscing elit, sed do eiusmod tempor incididunt ut labore et dolore magna aliqua. Ut enim ad minim veniam, quis nostrud exercitation ullamco laboris nisi ut aliquip ex ea commodo consequat. Duis aute irure dolor in reprehenderit in voluptate velit esse cillum dolore eu fugiat nulla pariatur. Excepteur sint occaecat cupidatat non proident, sunt in culpa qui officia deserunt mollit anim id est laborum</p>
  </div>
  <p class="footer-title">Presentation Title Goes Here</p>
  <div class="footer-bar"><span class="footer-bar__green"></span><span class="footer-bar__ink"></span></div>
  <div class="page-no">03</div>
</section>

</body>
</html>
```